Dialwell Hub
Web site
Project: Dialwell Hub
Dialwell Hub  - Telecommunications
Creative Brief
Telecommunications
Dialwell hub provides a hosted IVR(Integrated voice response) system for businesses. Think of when you call your credit card company and they ask you to enter your cc number, then they read you your balance, or let you select what you are calling about. That is what we provide. In addition, we provide automated calling solutions for companies who need to notify hundreds or thousands of people via phone or SMS text about topics (all opt-in). We are very much a web 2.0 saas company
I like www.pathmoxie.example website, www.safevane.example, tradeorbit.example, tallyfern.example. Corvix.example and quadrel.example are two big competitors. Looking very much for sass web2.0 look and feel.
green
white or grey
below header
pathmoxie.example
corvix.example
safevane.example
Pages on the site will be home, about us, contact us, products, services I am looking for both a home page and inside page design

```html
<!DOCTYPE html>
<html lang="en">
<head>
<meta charset="utf-8">
<title>Dialwell Hub – Hosted IVR</title>
<link rel="stylesheet" href="https://fonts.googleapis.com/css2?family=Arimo:wght@400;700&display=swap">
<style>
:root{
  --blue:#1c78c0;
  --blue-dark:#15548a;
  --blue-deep:#0e3f73;
  --green:#7ab52e;
  --orange:#f08a1c;
  --text:#555;
  --muted:#888;
  --line:#d9d9d9;
  --panel:#f3f3f3;
  --panel-dark:#e6e6e6;
  --white:#fff;
}
*{box-sizing:border-box;margin:0;padding:0}
html,body{width:1200px;height:1102px;overflow:hidden;background:var(--white);font-family:"Arimo",Arial,sans-serif;color:var(--text)}
.page{position:relative;width:1200px;height:1102px}
.abs{position:absolute}

/* header */
.brand{left:134px;top:34px;display:flex;align-items:center;gap:12px}
.brand-dot{width:44px;height:44px;border-radius:50%;background:var(--green)}
.brand-name{font-size:34px;font-weight:700;color:var(--blue-dark)}
.account{right:136px;top:4px;display:flex;gap:2px;background:var(--panel-dark);border-radius:0 0 6px 6px;padding:5px 10px;font-size:12px}
.account a{color:var(--blue-dark);text-decoration:none;font-weight:700;padding:0 7px;border-right:1px solid #bbb}
.account a:last-child{border-right:0}
.util{left:662px;top:84px;font-size:12px;color:var(--muted);display:flex;gap:22px}
.phone{right:136px;top:74px;display:flex;align-items:center;gap:10px;font-size:29px;font-weight:700;color:var(--blue-deep)}

/* nav */
.nav{left:134px;top:130px;width:930px;height:32px;background:linear-gradient(#fafafa,#e4e4e4);border:1px solid var(--line);border-radius:4px;display:flex;align-items:center;padding-left:10px}
.nav a{font-size:13px;color:#444;text-decoration:none;padding:0 30px;border-right:1px solid #ccc;line-height:16px}
.search{position:absolute;right:10px;top:5px;width:235px;height:21px;background:var(--white);border:1px solid #c6c6c6;border-radius:10px;font-size:12px;color:var(--blue-dark);font-weight:700;padding:2px 10px;display:flex;justify-content:space-between;align-items:center}

/* hero */
.hero{left:134px;top:178px;width:930px;height:316px;border-radius:6px;overflow:hidden;background:linear-gradient(180deg,#2d8fd8 0%,#1766b4 100%)}
.hero-photo{position:absolute;right:0;top:0;width:470px;height:316px;background:linear-gradient(90deg,rgba(45,143,216,0) 0%,#c9dbe9 35%,#e9eef3 100%)}
.hero h1{position:absolute;left:30px;top:22px;font-size:25px;color:var(--white);font-weight:700}
.hero .lead{position:absolute;left:30px;top:70px;width:410px;font-size:15px;line-height:19px;color:var(--white);font-weight:700}
.hero .small{position:absolute;left:30px;top:120px;width:380px;font-size:11px;line-height:14px;color:#dbe9f7;font-weight:700}
.try{position:absolute;left:30px;top:186px;width:222px;height:54px;border-radius:8px;background:linear-gradient(#ffa940,#e2700d);border:2px solid #f7c07a;display:flex;align-items:center;justify-content:space-between;padding:0 14px}
.try span{font-size:26px;font-weight:700;color:var(--white)}
.try i{width:30px;height:30px;border-radius:50%;background:var(--white);display:flex;align-items:center;justify-content:center}
.pager{position:absolute;left:30px;top:283px;display:flex;gap:4px}
.pager b{width:22px;height:20px;background:var(--white);color:var(--blue-dark);font-size:12px;display:flex;align-items:center;justify-content:center;border-radius:2px}
.pager b.on{background:var(--orange);color:var(--white)}

/* columns */
.box{top:535px;height:292px;border:1px solid var(--line);border-radius:4px;background:var(--white)}
.box-head{height:42px;background:linear-gradient(#fafafa,#ebebeb);border-bottom:1px solid var(--line);display:flex;align-items:center;gap:10px;padding-left:12px;font-size:18px;color:var(--blue-dark)}
.ico{width:26px;height:22px;border-radius:3px}
.box p{font-size:11px;line-height:13px}
.about p{padding:10px 12px 0}
.about strong{color:var(--blue-dark)}
.more{position:absolute;right:12px;bottom:8px;background:linear-gradient(#2c6fae,#15497d);color:var(--white);font-size:12px;font-weight:700;padding:5px 14px;border-radius:3px}
.news-item{margin:0 12px;padding:10px 0;border-bottom:1px dotted #bbb}
.news-item .date{font-size:11px;color:var(--blue-dark);font-weight:700;margin-bottom:3px}
.news-item p{font-size:11px;line-height:13px}
.news-item b{color:var(--blue-dark)}
.news-item em{font-style:normal;color:var(--blue)}

.newsletter{left:760px;top:535px;width:304px;height:142px;border:1px solid var(--line);border-radius:4px}
.newsletter p{font-size:10px;line-height:12px;color:var(--muted);padding:8px 12px 0}
.sub-row{position:absolute;left:12px;top:100px;display:flex;gap:6px}
.sub-row .field{width:196px;height:22px;border:1px solid #ccc;background:var(--white)}
.sub-row .btn{width:70px;height:22px;background:var(--panel-dark);border:1px solid #ccc;color:var(--orange);font-size:11px;font-weight:700;display:flex;align-items:center;justify-content:center}
.quote{left:760px;top:690px;width:304px;height:176px;background:var(--panel);border:1px solid var(--line);border-radius:4px}
.quote h3{font-size:16px;color:var(--blue-dark);font-weight:400;padding:10px 12px 0 46px}
.quote .mark{position:absolute;left:12px;top:8px;font-size:40px;color:#bbb;line-height:40px}
.quote p{font-size:11px;line-height:13px;font-style:italic;padding:14px 12px 0 46px}
.quote .by{position:absolute;left:110px;bottom:8px;font-size:11px;color:var(--muted)}

/* partners */
.partners{left:134px;top:910px;width:930px;height:76px;display:flex;justify-content:space-around;align-items:center}
.badge{height:46px;background:var(--panel-dark);border-radius:4px}
.badge.round{width:46px;border-radius:50%}

/* footer */
.foot{left:134px;top:1004px;width:930px;height:32px;background:linear-gradient(#f7f7f7,#e7e7e7);border:1px solid var(--line);border-radius:4px;display:flex;align-items:center;padding-left:12px}
.foot a{font-size:12px;color:var(--blue-dark);text-decoration:none;padding:0 14px 0 0;margin-right:14px;border-right:1px solid #ccc}
.connect{position:absolute;right:10px;top:7px;display:flex;align-items:center;gap:6px;font-size:12px;color:#444}
.connect i{width:18px;height:18px;border-radius:3px;background:#9aa6b2}
.legal{left:0;top:1058px;width:1200px;text-align:center;font-size:11px;line-height:15px;color:var(--muted)}
</style>
</head>
<body>
<div class="page">

  <header>
    <div class="abs brand"><span class="brand-dot"></span><span class="brand-name">Dialwell Hub</span></div>
    <nav class="abs account"><a href="#">Live Chat</a><a href="#">Login</a><a href="#">Register</a></nav>
    <div class="abs util"><span>Customer Support</span><span>Help</span></div>
    <div class="abs phone">
      <svg width="26" height="26" viewBox="0 0 24 24"><circle cx="12" cy="12" r="12" fill="#1c78c0"/><path d="M8 6c1 0 2 2 2 3s-1 1-1 2 2 4 4 4 1-1 2-1 3 1 3 2-1 2-3 2c-4 0-9-5-9-9 0-2 1-3 2-3z" fill="#fff"/></svg>
      1-800-555-0142
    </div>
  </header>

  <nav class="abs nav">
    <a href="#">Home</a><a href="#">About Us</a><a href="#">Products</a><a href="#">Services</a><a href="#">Contact Us</a>
    <div class="search">Search
      <svg width="14" height="14" viewBox="0 0 14 14"><circle cx="6" cy="6" r="4.5" stroke="#15548a" stroke-width="2" fill="none"/><path d="M9.5 9.5L13 13" stroke="#15548a" stroke-width="2"/></svg>
    </div>
  </nav>

  <section class="abs hero">
    <div class="hero-photo" role="img" aria-label="Photo of smiling support agents wearing headsets in a bright office"></div>
    <h1>Lorem Ipsum Sit Dolor Nectum</h1>
    <p class="lead">15000 Firmen und Institutionen die uns vertrauen dolog semog eman de.</p>
    <p class="small">Lorem ipsum dolor sit amet, sed do consectetur et dolore adipiscing conse cetur et dolore ut labore et dolore.</p>
    <div class="try"><span>TRY NOW!</span><i><svg width="14" height="14" viewBox="0 0 14 14"><path d="M4 2l6 5-6 5z" fill="#e2700d"/></svg></i></div>
    <div class="pager"><b>1</b><b class="on">2</b><b>3</b><b>4</b><b>5</b></div>
  </section>

  <section class="abs box about" style="left:134px;width:284px">
    <div class="box-head"><span class="ico" style="background:var(--blue)"></span>About Dialwell Hub</div>
    <p><strong>Lorem consectetur adipiscing elit,</strong> sed do eiusmod tempor incididunt ut labore et dolore magna aliqua. Ut enim ad minim veniam, quis nostrud exercitation ullamco laboris nisi ut aliquip ex ea commodo consequat. Duis aute irure dolor in reprehenderit in voluptate velit esse cillum dolore eu fugiat nulla pariatur. Excepteur sint occaecat cupidatat non proident, sunt in culpa qui officia deserunt mollit anim id est laborum et dolore magna.</p>
    <p>Sed ut perspiciatis unde omnis iste natus error sit voluptatem accusantium doloremque laudantium, totam rem aperiam eaque ipsa quae ab illo inventore.</p>
    <span class="more">Read More</span>
  </section>

  <section class="abs box news" style="left:447px;width:284px">
    <div class="box-head"><span class="ico" style="background:var(--blue-dark)"></span>News and Events</div>
    <div class="news-item"><div class="date">May 25, 2011</div><p><b>Lorem ipsum dolor sit amet, sed do</b> consectetur et dolore adipiscing. <em>Learn More</em></p></div>
    <div class="news-item"><div class="date">May 25, 2011</div><p><b>Lorem ipsum dolor sit amet, sed do</b> consectetur et dolore adipiscing. <em>Learn More</em></p></div>
    <div class="news-item" style="border:0"><div class="date">May 25, 2011</div><p><b>Lorem ipsum dolor sit amet, sed do</b> consectetur et dolore adipiscing. <em>Learn More</em></p></div>
    <span class="more">Read More</span>
  </section>

  <section class="abs newsletter">
    <div class="box-head"><span class="ico" style="background:var(--orange)"></span>Join Our Newsletter</div>
    <p>Lorem Ipsum Sit Dolor Nectum sed eiusmod tempor incididunt ut labore et dolore magna aliqua.</p>
    <div class="sub-row"><span class="field"></span><span class="btn">Subscribe</span></div>
  </section>

  <section class="abs quote">
    <span class="mark">&ldquo;</span>
    <h3>Excellent Service &amp; Consulting</h3>
    <p>sed do eiusmod tempor incididunt ut labore et dolore magna aliqua. Ut enim ad minim veniam quis nostrud exercitation ullamco laboris.</p>
    <span class="by">- Dana Merritt, CEO</span>
  </section>

  <section class="abs partners" aria-label="Partner badges">
    <span class="badge" style="width:120px"></span>
    <span class="badge round"></span>
    <span class="badge" style="width:150px"></span>
    <span class="badge" style="width:110px"></span>
    <span class="badge" style="width:170px"></span>
  </section>

  <footer>
    <nav class="abs foot">
      <a href="#">Support</a><a href="#">Data Center</a><a href="#">Terms</a><a href="#">Career Corporation</a><a href="#" style="border:0">About Us</a>
      <div class="connect">Connect with Us <i></i><i></i><i></i><i></i></div>
    </nav>
    <p class="abs legal">DialwellHub.com® Putting the Caller First! Dialwell Hub, Inc. is a subsidiary of Northlake Systems Incorporated.<br>© 2000-2010, Dialwell Hub.com Incorporated. All rights reserved.</p>
  </footer>

</div>
</body>
</html>
```